Webbanner-Design für regionale Geschenkkarte
Zielgruppe
Die Lindgrün-Karte ist eine regionale Geschenkkarte für PLZ 52 zur Unterstützung aller inhabergeführten Geschäfte wie Einzelhandel, Restaurants und Dienstleister
Zielgruppe sind all diejenigen, die eine Geschenkkarte suchen und die das regionale den Internetriesen und Großfilialisten vorziehen. Zudem können die Verschenker auch ein individuelles Design erhalten. Über unsere App können die Kunden Bilder hochladen, individuelle Texte auf die Karte drucken lassen etc.
Aufgabenstellung
Regionale Geschenkkarte PLZ 52 (www.lindgruen-karte.example) , individuelles Design, verschiedene Bannergrößen wichtig zum Einbau auf Unterseiten von Kunden der lindgruenpix.example, zudem sollen die Banner auch direkt auf Seiten der Kunden eingebaut werden können. Nach dem Motto: wir akzeptieren die Lindgrün Geschenkkarte bzw. wir sind dabei

```html
<!DOCTYPE html>
<html lang="de">
<head>
<meta charset="utf-8">
<title>Lindgrün-Karte – Webbanner</title>
<link rel="stylesheet" href="https://fonts.googleapis.com/css2?family=Noto+Sans:wght@700&family=PT+Sans+Narrow:wght@700&family=Arimo&display=swap">
<style>
  :root {
    --page-bg: #ebf0f8;
    --red-deep: #a00a1a;
    --red-mid: #c41b30;
    --red-light: #e5474f;
    --red-text: #8c0b17;
    --white: #ffffff;
    --photo-hair: #4a302b;
    --photo-skin: #d9a58c;
    --photo-shirt: #bfe0e4;
  }
  * { margin: 0; padding: 0; box-sizing: border-box; }
  html, body { width: 1200px; height: 699px; overflow: hidden; background: var(--page-bg); }
  .banner {
    position: absolute; left: 155px; top: 34px; width: 899px; height: 635px;
    overflow: hidden;
    background:
      radial-gradient(ellipse 260px 220px at 160px 290px, rgba(255,255,255,0.55), rgba(255,255,255,0) 70%),
      linear-gradient(180deg, var(--red-deep) 0%, #b2304a 28%, #d99aa6 55%, #ffffff 80%, #ffffff 100%);
  }
  .brand { position: absolute; left: 27px; top: 17px; display: flex; align-items: center; }
  .brand-square {
    width: 117px; height: 116px; border-radius: 10px;
    background: linear-gradient(135deg, var(--red-deep), var(--red-light));
  }
  .brand-name {
    margin-left: 22px; margin-top: -12px;
    font-family: "Noto Sans", sans-serif; font-weight: 700; font-size: 47px;
    color: var(--white); letter-spacing: 1px;
  }
  .headline {
    position: absolute; right: 38px; top: 126px; line-height: 1;
    font-family: "PT Sans Narrow", sans-serif; font-weight: 700; font-size: 38px;
    color: var(--white);
  }
  .gift-card {
    position: absolute; left: 316px; top: 185px; width: 564px; height: 365px;
    border-radius: 15px; overflow: hidden;
    background: linear-gradient(155deg, var(--red-deep) 0%, var(--red-mid) 45%, var(--red-light) 100%);
    box-shadow: 2px 4px 6px rgba(0,0,0,0.35);
  }
  .ribbon-v { position: absolute; left: 146px; top: 0; width: 34px; height: 100%; background: var(--white); }
  .ribbon-h { position: absolute; left: 0; top: 107px; width: 100%; height: 32px; background: var(--white); }
  .card-url {
    position: absolute; right: 17px; top: 82px;
    font-family: "Noto Sans", sans-serif; font-weight: 700; font-size: 13px; color: var(--white);
  }
  .card-title {
    position: absolute; right: 17px; top: 101px;
    font-family: "Noto Sans", sans-serif; font-weight: 700; font-size: 32px; color: var(--red-text);
    letter-spacing: 0.5px; line-height: 1.3;
  }
  .card-code {
    position: absolute; right: 17px; bottom: 22px;
    font-family: "Arimo", sans-serif; font-size: 18px; color: var(--white);
  }
  .photo { position: absolute; left: 0; top: 0; width: 899px; height: 635px; pointer-events: none; }
  .web-address {
    position: absolute; right: 20px; bottom: 14px;
    font-family: "PT Sans Narrow", sans-serif; font-weight: 700; font-size: 43px;
    color: var(--red-text);
  }
</style>
</head>
<body>
  <main class="banner">
    <div class="brand">
      <div class="brand-square"></div>
      <span class="brand-name">Lindgrün-Karte</span>
    </div>
    <h1 class="headline">Die regionale Geschenkkarte für PLZ 52</h1>

    <div class="gift-card">
      <div class="ribbon-v"></div>
      <div class="ribbon-h"></div>
      <span class="card-url">lindgruen-karte.example</span>
      <span class="card-title">Geschenkkarte</span>
      <span class="card-code">SMS</span>
    </div>

    <svg class="photo" viewBox="0 0 899 635" role="img" aria-label="Foto: lächelnde Frau mit langen dunklen Haaren hält eine Geschenkkarte in die Kamera">
      <defs>
        <linearGradient id="photoTone" x1="0" y1="0" x2="0" y2="1">
          <stop offset="0" stop-color="var(--photo-hair)"/>
          <stop offset="0.45" stop-color="var(--photo-skin)"/>
          <stop offset="0.8" stop-color="var(--photo-shirt)"/>
          <stop offset="1" stop-color="var(--photo-shirt)"/>
        </linearGradient>
      </defs>
      <rect x="0" y="190" width="470" height="470" rx="40" fill="url(#photoTone)"/>
    </svg>

    <div class="web-address">www.lindgruen-karte.example</div>
  </main>
</body>
</html>
```